Building Company Business Card Design

I am looking to get a business card designed for my Building Company. Please find the logo attached.

Industry/Entity Type

Business

Contact Information for Business Card

Mobile 0472 913 706
Email admin@harbourlineconstruct.com.au
Website www.harbourlineconstruct.com.au

Colors
0255a3

```html
<!DOCTYPE html>
<html lang="en">
<head>
<meta charset="utf-8">
<title>Harbourline Construct – Business Card</title>
<link rel="stylesheet" href="https://fonts.googleapis.com/css2?family=Montserrat:wght@400;500;700&display=swap">
<style>
  :root {
    --brand-blue: #0255a3;
    --steel-grey: #8f9092;
    --ink: #3a3a3c;
    --paper: #ffffff;
    --backdrop: #ececee;
  }
  * { margin: 0; padding: 0; box-sizing: border-box; }
  html, body {
    width: 1200px; height: 874px; overflow: hidden;
    background: var(--backdrop);
    font-family: "Montserrat", sans-serif;
  }
  .card-set {
    position: relative; width: 1200px; height: 874px;
    display: flex; align-items: center; justify-content: center; gap: 60px;
  }
  .card {
    position: relative; width: 520px; height: 318px;
    box-shadow: 0 10px 30px rgba(0,0,0,.18);
    overflow: hidden;
  }
  /* Front */
  .card-front {
    background: var(--brand-blue); color: var(--paper);
    display: flex; flex-direction: column; align-items: center; justify-content: center;
  }
  .card-front .brand-name {
    font-weight: 700; font-size: 34px; letter-spacing: 1px; text-transform: uppercase;
    line-height: 1.1; text-align: center;
  }
  .card-front .website {
    margin-top: 46px; font-size: 13px; font-weight: 400; letter-spacing: .3px;
  }
  /* Back */
  .card-back { background: var(--paper); color: var(--ink); }
  .band { position: absolute; left: 0; width: 100%; height: 16px; display: flex; }
  .band-top { top: 0; }
  .band-bottom { bottom: 0; }
  .band span { display: block; height: 100%; }
  .band .blue { background: var(--brand-blue); }
  .band .grey { background: var(--steel-grey); }
  .band-top .blue { width: 52%; }
  .band-top .grey { width: 48%; }
  .band-bottom .grey { width: 33%; }
  .band-bottom .blue { width: 67%; }
  .card-back .brand-name {
    position: absolute; left: 42px; top: 92px;
    font-weight: 700; font-size: 26px; letter-spacing: .5px; text-transform: uppercase;
    color: var(--brand-blue); line-height: 1.1;
  }
  .contact-list {
    position: absolute; left: 190px; top: 178px;
    list-style: none; font-size: 13px; line-height: 24px;
  }
  .contact-list .label {
    display: inline-block; width: 22px; font-weight: 700; color: var(--brand-blue);
  }
</style>
</head>
<body>
  <main class="card-set">
    <section class="card card-front" aria-label="Card front">
      <h1 class="brand-name">Harbourline<br>Construct</h1>
      <p class="website">www.harbourlineconstruct.com.au</p>
    </section>

    <section class="card card-back" aria-label="Card back">
      <div class="band band-top"><span class="blue"></span><span class="grey"></span></div>
      <h2 class="brand-name">Harbourline<br>Construct</h2>
      <ul class="contact-list">
        <li><span class="label">M:</span>0472 913 706</li>
        <li><span class="label">E:</span>admin@harbourlineconstruct.com.au</li>
        <li><span class="label">W:</span>www.harbourlineconstruct.com.au</li>
      </ul>
      <div class="band band-bottom"><span class="grey"></span><span class="blue"></span></div>
    </section>
  </main>
</body>
</html>
```